Finally a Vodka produced for women ! (Label Design)

We are a small distillery based in Melbourne, Australia and we need a Vodka label design solution that will appeal to women aged 30-50 years and radiate luxury. Full Details are in a design brief attached. We thank you in advance.

Target Market(s)

Affluent females 30-50 years.

Industry/Entity Type

Spirits/Alcohol

Requirements
Must have
• Be clear this is a luxury Vodka.
Nice to have
• Elegance.

```html
<!DOCTYPE html>
<html lang="en">
<head>
<meta charset="utf-8">
<title>Violet Crest Distillery – Vodka Label</title>
<link href="https://fonts.googleapis.com/css2?family=Montserrat:wght@600;700&family=Alegreya:wght@400&display=swap" rel="stylesheet">
<style>
  :root {
    --stage: #7d537e;
    --peach: #efb894;
    --rose: #c9979a;
    --mauve: #a07f9f;
    --violet: #7a6399;
    --indigo: #5a4a86;
    --ink: #231f22;
    --label-text: #f1eef3;
  }
  html, body {
    margin: 0;
    width: 1200px;
    height: 1200px;
    overflow: hidden;
    background: var(--stage);
  }
  .canvas {
    position: relative;
    width: 1200px;
    height: 1200px;
    background: var(--stage);
  }
  .label-shadow {
    position: absolute;
    left: 262px;
    top: 82px;
    width: 676px;
    height: 1036px;
    filter: drop-shadow(0 18px 30px rgba(40, 20, 50, 0.35));
  }
  .label {
    position: relative;
    width: 100%;
    height: 100%;
    clip-path: polygon(50% 0, 100% 81.8%, 69% 100%, 31% 100%, 0 81.8%);
  }
  .facet-fill {
    position: absolute;
    inset: 0;
    background: linear-gradient(180deg,
      var(--peach) 0%,
      #e6ad92 30%,
      var(--rose) 55%,
      var(--mauve) 72%,
      var(--violet) 86%,
      var(--indigo) 100%);
  }
  .brand-mark {
    position: absolute;
    left: 0;
    right: 0;
    top: 250px;
    margin: 0;
    text-align: center;
    font-family: "Montserrat", sans-serif;
    font-weight: 700;
    font-size: 24px;
    line-height: 1.25;
    letter-spacing: 0.14em;
    color: var(--ink);
  }
  .brand-mark span {
    display: block;
    margin-right: -0.14em;
  }
  .brand-name {
    position: absolute;
    left: 0;
    right: 0;
    top: 560px;
    margin: 0;
    text-align: center;
    font-family: "Montserrat", sans-serif;
    font-weight: 700;
    color: var(--label-text);
    line-height: 1;
  }
  .brand-name span { display: block; }
  .brand-name .line-first {
    font-size: 62px;
    letter-spacing: 0.24em;
    margin-right: -0.24em;
  }
  .brand-name .line-second {
    font-size: 80px;
    letter-spacing: 0.12em;
    margin-right: -0.12em;
    margin-top: 8px;
  }
  .brand-name .line-third {
    font-size: 34px;
    font-weight: 600;
    letter-spacing: 0.5em;
    margin-right: -0.5em;
    margin-top: 24px;
  }
  .strength {
    position: absolute;
    left: 0;
    right: 0;
    top: 850px;
    margin: 0;
    text-align: center;
    font-family: "Alegreya", serif;
    font-size: 24px;
    color: var(--label-text);
    letter-spacing: 0.02em;
  }
  .strength .abv {
    font-size: 44px;
    margin: 0 8px;
    vertical-align: -4px;
  }
</style>
</head>
<body>
  <main class="canvas">
    <div class="label-shadow">
      <section class="label">
        <div class="facet-fill" role="img" aria-label="Low-poly faceted gem pattern shading from peach at the top to violet at the base"></div>
        <p class="brand-mark"><span>VIOLET</span><span>CREST</span></p>
        <h1 class="brand-name">
          <span class="line-first">VIOLET</span>
          <span class="line-second">CREST</span>
          <span class="line-third">DISTILLERY</span>
        </h1>
        <p class="strength">ALCOHOL<span class="abv">40%</span>BY VOL.</p>
      </section>
    </div>
  </main>
</body>
</html>
```